All Natural Raw Honey & Goats Milk Body Wash Labels

We have launched a new product line of all natural Raw Honey & Goats Milk body wash with the business name being Dawn Meadow and the tag line Naturally . Their are currently three line items requiring three labels. Natural (Unscented), Japanese Honeysuckle and Caribbean.
It is a family orientated product that we want to promote as being all natural, healthy and trustworthy. It is an all Australian made product that uses our very own award winning raw honey
I can supply the file for the business name/logo upon request

Target Market(s)

Families

Industry/Entity Type

Bath & body

Requirements
Must have
• a Lux high end feel
Nice to have
• simple easy to read with minimal images
Should not have
• No cartoons

```html
<!DOCTYPE html>
<html lang="en">
<head>
<meta charset="utf-8">
<title>Dawn Meadow – Raw Honey &amp; Goats Milk Body Wash Label</title>
<link rel="stylesheet" href="https://fonts.googleapis.com/css2?family=Open+Sans:wght@300;400&family=Poppins:wght@600;700&display=swap">
<style>
  :root {
    --canvas-bg: #eceef0;
    --label-bg: #ffffff;
    --honey: #f9cf0a;
    --honey-band: #fcd83a;
    --blob-main: #fddc4a;
    --blob-soft: #fde98f;
    --drip: #f1f1f1;
    --ink: #111111;
  }
  * { margin: 0; padding: 0; box-sizing: border-box; }
  html, body {
    width: 1200px;
    height: 797px;
    overflow: hidden;
    background: var(--canvas-bg);
  }
  .label {
    position: absolute;
    left: 390px;
    top: 17px;
    width: 420px;
    height: 762px;
    background: var(--label-bg);
    overflow: hidden;
    box-shadow: 0 2px 12px rgba(0,0,0,0.08);
  }
  .band-top {
    position: absolute;
    left: 0; right: 0; top: 0;
    height: 10px;
    background: var(--honey-band);
  }
  .drip-decoration {
    position: absolute;
    left: 0; right: 0; top: 10px;
    height: 370px;
    background: linear-gradient(180deg, var(--drip) 0%, #f6f6f6 55%, rgba(255,255,255,0) 100%);
  }
  .brand {
    position: absolute;
    left: 0; right: 0; top: 118px;
    text-align: center;
    font-family: "Open Sans", sans-serif;
    font-weight: 400;
    font-size: 40px;
    letter-spacing: 1px;
    color: var(--ink);
  }
  .product-name {
    position: absolute;
    left: 0; right: 0; top: 236px;
    text-align: center;
    font-family: "Open Sans", sans-serif;
    font-weight: 400;
    color: var(--honey);
    line-height: 1;
  }
  .product-name .line-1 { display: block; font-size: 44px; }
  .product-name .line-2 { display: block; font-size: 51px; margin-top: 8px; }
  .product-type {
    position: absolute;
    left: 0; right: 0; top: 348px;
    text-align: center;
    font-family: "Open Sans", sans-serif;
    font-weight: 400;
    font-size: 23px;
    letter-spacing: 0.5px;
    color: var(--ink);
  }
  .scent-badge {
    position: absolute;
    left: 56px;
    top: 396px;
    width: 275px;
    height: 262px;
  }
  .scent-badge svg { position: absolute; inset: 0; }
  .scent-name {
    position: absolute;
    left: 0; right: 0; top: 70px;
    text-align: center;
    font-family: "Poppins", sans-serif;
    font-weight: 700;
    font-size: 29px;
    line-height: 1.18;
    color: var(--ink);
  }
  .claim {
    position: absolute;
    left: 0; right: 0; top: 668px;
    text-align: center;
    font-family: "Open Sans", sans-serif;
    font-weight: 400;
    font-size: 23px;
    color: var(--ink);
  }
  .band-bottom {
    position: absolute;
    left: 0; right: 0; bottom: 0;
    height: 33px;
    background: var(--honey-band);
    text-align: center;
    font-family: "Poppins", sans-serif;
    font-weight: 700;
    font-size: 17px;
    line-height: 35px;
    color: var(--ink);
  }
</style>
</head>
<body>
  <main class="label">
    <div class="band-top"></div>
    <div class="drip-decoration" role="img" aria-label="Faint grey honey drips running down from the top of the label"></div>

    <div class="brand">Dawn Meadow</div>

    <h1 class="product-name">
      <span class="line-1">RAW HONEY &amp;</span>
      <span class="line-2">GOATS MILK</span>
    </h1>
    <p class="product-type">BODY WASH</p>

    <div class="scent-badge">
      <svg viewBox="0 0 275 262" width="275" height="262" aria-hidden="true">
        <path fill="var(--blob-soft)" opacity="0.85"
          d="M30 70 C60 20 140 0 200 12 C255 24 280 80 270 140 C262 200 220 250 160 258 C100 266 40 240 18 190 C-2 145 4 105 30 70 Z"/>
        <path fill="var(--blob-main)" opacity="0.9"
          d="M20 105 C30 50 90 22 150 18 C210 14 255 50 258 110 C262 170 232 225 180 245 C125 266 60 248 30 205 C8 175 12 140 20 105 Z"/>
      </svg>
      <h2 class="scent-name">JAPANESE<br>HONEYSUCKLE</h2>
    </div>

    <p class="claim">100% NATURAL</p>
    <div class="band-bottom">12 fl oz.</div>
  </main>
</body>
</html>
```